Lantern Harvest CD design

I need a CD cover & sleeve design for an upcoming February 2014 CD release event (at a music store). This is a collection of original songs written and sung by yours truly. Many songs are inspired by my ancestors, although there are a few songs that are just about life and love. We are all a product of our ancestry, and we carry this history in our hearts whether we think it influences us or not. This is my first CD although I've been singing and performing for over 30 years, and this body of work is where I'm at now musically and creatively. I'm proud of the effort I've made and want to present myself as someone who is real and genuine. My design style tends towards simple, clean, uncluttered lines, sans serif type faces. No loud or saturated colors please, no reds or pinks. I love the blues & greens. I have a sepia image in my head, but maybe because I've been looking at old photos of my grandparents as inspiration for the last 6 months...!

I am including two shots of me, and some old photos that could be used as a design element, but not mandatory. I wanted you to have some choices... I also have a lot of CD liner notes, but am willing to edit if I need to. This would need to be in 4 color with a sleeve that flaps open, and a lift of something similar for CD imprint. Sorry about the tight deadline, I have to get a print run done before the launch and that lead time is ridiculously tight. If you want an mp3 sample of one song I am happy to forward to give you an idea of my sound, it might help to inspire if you're a music person :-) just let me know at megtalvinatpostvellidotcom

Update for inside text: Cover photo by Daniel Kopreth, others photos taken by Meg Talvin.

Target Market(s)

Anyone who likes original singer / songwriter music, fellow music lovers, audience members after a performance. My influence is only in the northeast US thus far.

Industry/Entity Type

Store

Requirements
Must have
• Title of CD: Lantern Harvest

Name: Meg Talvin

lower left back corner - leave 1-1/4"x1/2" room in design on back cover for UPC barcode
Nice to have
• A lighter touch, artistic vibe, softer painterly approach, Don't mind the blue / green spectrum, or a sepia toned feel. Some music folks feedback has inspired me to update this: I need o have my face on the cover! the b&w shot is a little better. And it would be nice to incorporate both sets of ancestor pictures in some way. (The faded grandma and young boy and the couple with flowers that I am holding).
Song list on the back is helpful, too.
Should not have
• No loud, saturated colors, no reds or pinks please.

```html
<!DOCTYPE html>
<html lang="en">
<head>
<meta charset="utf-8">
<title>Lantern Harvest – Liner Notes</title>
<link rel="stylesheet" href="https://fonts.googleapis.com/css2?family=Arimo:wght@400;700&display=swap">
<style>
  :root {
    --page: #ffffff;
    --panel: #3d3532;
    --ink: #cdc8c4;
    --heading: #d6d2cf;
    --frame: #ffffff;
    --mill-a: #8a8378;
    --mill-b: #5e5a52;
    --portrait-a: #8c8c8c;
    --portrait-b: #3c3c3c;
    --family-a: #9fb0b4;
    --family-b: #6d6a5e;
  }
  html, body {
    margin: 0;
    width: 1200px;
    height: 1200px;
    overflow: hidden;
    background: var(--page);
  }
  .liner-panel {
    position: absolute;
    left: 117px;
    top: 117px;
    width: 964px;
    height: 960px;
    background: var(--panel);
    font-family: "Arimo", Arial, sans-serif;
    color: var(--ink);
    font-size: 13.4px;
    line-height: 17px;
  }
  .block {
    position: absolute;
    left: 72px;
    width: 826px;
    margin: 0;
  }
  .block p { margin: 0; }
  .song-notes { top: 47px; }
  .song-notes p { margin-bottom: 6px; }
  .song-title {
    font-size: 18px;
    font-weight: 700;
    color: var(--heading);
    line-height: 1;
  }
  .acoustic-credits { top: 275px; }
  .footnotes { top: 412px; }
  .blues-credits { top: 516px; }
  .thanks { top: 775px; }
  .photo {
    position: absolute;
  }
  .photo-mill {
    left: 301px; top: 665px; width: 165px; height: 92px;
    background: linear-gradient(180deg, #a9a79f 0%, var(--mill-a) 45%, var(--mill-b) 100%);
  }
  .photo-portrait {
    left: 483px; top: 608px; width: 143px; height: 143px;
    border: 3px solid var(--frame);
    background: radial-gradient(circle at 50% 40%, var(--portrait-a) 0%, var(--portrait-b) 100%);
  }
  .photo-family {
    left: 651px; top: 608px; width: 249px; height: 155px;
    background: linear-gradient(135deg, var(--family-a) 0%, #8e9387 50%, var(--family-b) 100%);
  }
</style>
</head>
<body>
<main class="liner-panel">
  <section class="block song-notes">
    <p><span class="song-title">Heading Home</span> is a song about me and my dad (he passed in 2011). He had a unique life long before I came along. I’m not sure I fully knew who he was. I miss him but he watches over.</p>
    <p><span class="song-title">Barynya</span> *, which is Russian for “barn dance” and “sudarnya” for “young lady” is a song about my grandmother Raisa, who emigrated from Russia to Ellis Island, NY, then made her way south to start her life over after an Odessa pogrom**.</p>
    <p><span class="song-title">Mountain Gal</span> is a song about my elderly mom who is facing the end of her life, which is not as sad as you might imagine, since passing is just another part of life. I cherish her.</p>
    <p><span class="song-title">Slow Down</span> is my reminder to pay attention, especially to the people I love the most and often take for granted.</p>
    <p><span class="song-title">Crazy Fool</span> is about redemption and the guy who got away.</p>
    <p><span class="song-title">Love Is Weeping</span> is for Nora and her sisters.</p>
    <p><span class="song-title">Sweet Sue</span> is a favorite old song of mine, and a nice way to end the day…thinking of “just you”.</p>
  </section>

  <section class="block acoustic-credits">
    <p>Meg Talvin – vocals and harmony</p>
    <p>Glen Harrow – acoustic guitar player &amp; founder of Acoustic Fernbrook in CT. Glen inspired me to start Acoustic Millbrook, a similar acoustic program that gives back to millbrookarts.org. Glen is a living example of how to play it forward, and I thank him for his musical input and arranging.</p>
    <p>Owen Pratt, Brookfield, CT – violin</p>
    <p>Neil Varsky – acoustic bass &amp; Toby Varsky – mandolin on Barynya and Mountain Gal &amp; guitar on Sweet Sue</p>
    <p>Lila Jo Marchetti – harmony on Heading Home &amp; Barynya</p>
  </section>

  <section class="block footnotes">
    <p>*The violin intro and inspiration for writing Barynya is taken from the intro to Czardas written by Italian composer Aurelio Santini in 1904.</p>
    <p>**A pogrom is a violent massacre or persecution of an ethnic or religious group, particularly one aimed at Jews. The term, a Yiddish variation on a Russian word meaning “thunder”, originally entered the English language to describe 19th and 20th-century attacks on Jews in the Russian Empire.</p>
  </section>

  <section class="block blues-credits">
    <p>Oh My Love, Tailspin, and Got To Prove Blues</p>
    <p>These three songs explore the human condition of relationships, and I like blues progressions. The more I know, the less I know, especially when it comes to matters of the heart. We are all a work in progress, no?</p>
    <p>Hal “Rook” Denner, Westport, CT &amp; Austin, TX – electric guitar</p>
    <p>Curtis Fennel, Weston, CT &amp; Chicago, IL – electric guitar Guest Jonah Pellick – organ on Got To Prove Blues</p>
    <p>Evan Strand, Norwalk, CT – electric bass</p>
    <p>Miles Corrado, New York, NY – drums</p>
    <p>Lila Jo Marchetti – harmony on Oh My Love</p>
    <p>Meg Talvin – vocals, harmony</p>
  </section>

  <div class="photo photo-mill" role="img" aria-label="Old photograph of an industrial mill with smokestack"></div>
  <div class="photo photo-portrait" role="img" aria-label="Black and white portrait of the singer"></div>
  <div class="photo photo-family" role="img" aria-label="Faded vintage photograph of a grandmother with a young boy"></div>

  <section class="block thanks">
    <p>I want to thank my four children and their mates for their support and love; and my beautiful mom who is showing me how to grow old gracefully. Also thanks to my friend Dana who has listened to countless ideas with an ear for critique; my friend Ruth who saw that I had to share my music and inspired me to do so; Glen Harrow who is a musical-feel-vibe-genius guitar guru, and Lila Jo Marchetti, my raven-haired, magical daughter who provides harmony on some of the tunes. Lastly, to my husband Walt, who is an authentic, generous, real man. I hope you all find something you like. Never, ever, stop creating and sharing your heart.</p>
    <p>Talk to me at megtalvin@postvelli.com</p>
  </section>
</main>
</body>
</html>
```